Coffee label for grocery store sales

We need a 3x4 label designed for our expanding grocery store market. I'm looking for something playful that will be eye catching on a shelf. Bag color is negotiable, but would prefer kraft, white, or black.

Target Market(s)

Grocery Stores

Industry/Entity Type

Coffee Shop

Logo Text

Heron Lane Coffee

Colors

Designer to choose colors to be used in the design.

Requirements
Must have
• Space for address label to identify blend.
• 47 W. Oak Ave., Dunmore, WI 54921
• www.heronlanecoffee.example
Nice to have
• Illustrations, bold colors

```html
<!DOCTYPE html>
<html lang="en">
<head>
<meta charset="utf-8">
<title>Heron Lane Coffee – Bag Label</title>
<link rel="stylesheet" href="https://fonts.googleapis.com/css2?family=Cinzel:wght@400;700&display=swap">
<style>
  :root {
    --page: #ffffff;
    --label-base: #b07a5e;
    --band: #b98166;
    --swirl-dark: #5c3522;
    --swirl-mid: #a4663f;
    --swirl-light: #f1c791;
    --ink-light: #fbeee2;
    --logo-panel: #ffffff;
    --logo-ink: #1e1410;
    --cup-dark: #2a1810;
    --cup-mid: #5a3826;
    --cup-rim: #efe9e2;
  }
  * { margin: 0; padding: 0; box-sizing: border-box; }
  html, body {
    width: 1200px;
    height: 2338px;
    overflow: hidden;
    background: var(--page);
  }
  .label {
    position: absolute;
    left: 120px;
    top: 530px;
    width: 960px;
    height: 1277px;
    background: var(--label-base);
    overflow: hidden;
    font-family: "Cinzel", Georgia, serif;
    color: var(--ink-light);
  }
  .label__pattern {
    position: absolute;
    inset: 0;
    background:
      radial-gradient(circle at 20% 25%, var(--swirl-light) 0 8%, transparent 22%),
      radial-gradient(circle at 80% 60%, var(--swirl-light) 0 6%, transparent 20%),
      radial-gradient(circle at 30% 80%, var(--swirl-mid) 0 10%, transparent 28%),
      linear-gradient(160deg, var(--swirl-mid), var(--swirl-dark) 55%, var(--swirl-mid));
  }
  .label__band {
    position: absolute;
    left: 290px;
    top: 0;
    width: 380px;
    height: 833px;
    background: var(--band);
    border-radius: 0 0 40px 40px;
  }
  .label__story {
    position: absolute;
    left: 300px;
    top: 14px;
    width: 360px;
    font-size: 13.5px;
    line-height: 22px;
    text-align: center;
    text-transform: uppercase;
    letter-spacing: 0.3px;
  }
  .brand-panel {
    position: absolute;
    left: 304px;
    top: 152px;
    width: 352px;
    height: 180px;
    background: var(--logo-panel);
    border: 5px solid var(--logo-ink);
    border-radius: 12px;
    display: flex;
    align-items: center;
    justify-content: center;
    text-align: center;
  }
  .brand-panel__name {
    font-family: "Cinzel", Georgia, serif;
    font-weight: 700;
    font-size: 44px;
    line-height: 52px;
    color: var(--logo-ink);
  }
  .motto {
    position: absolute;
    left: 280px;
    top: 400px;
    width: 400px;
    height: 400px;
  }
  .motto text {
    fill: var(--ink-light);
    font-family: "Cinzel", Georgia, serif;
    font-size: 24px;
    letter-spacing: 3px;
  }
  .cup-art {
    position: absolute;
    left: 330px;
    top: 450px;
    width: 300px;
    height: 300px;
    border-radius: 50%;
    background: radial-gradient(circle at 50% 50%, var(--cup-dark) 0 55%, var(--cup-mid) 72%, var(--cup-rim) 82%);
  }
  .address-strip {
    position: absolute;
    left: 162px;
    top: 1177px;
    width: 636px;
    height: 92px;
    background: var(--band);
    display: flex;
    flex-direction: column;
    justify-content: center;
    align-items: center;
    font-size: 27px;
    line-height: 40px;
    letter-spacing: 1px;
    text-transform: uppercase;
  }
</style>
</head>
<body>
  <main class="label">
    <div class="label__pattern" role="img" aria-label="Hand-drawn swirling pattern in cream, caramel and dark brown covering the label"></div>
    <div class="label__band"></div>

    <p class="label__story">At Heron Lane Coffee, each cup is doted upon, start to finish. Using coffee beans that have been ethically sourced from around the globe. Our roast masters fire up the custom built single-pass fluid bed roaster to create a clean, complex cup.</p>

    <div class="brand-panel">
      <h1 class="brand-panel__name">Heron Lane<br>Coffee</h1>
    </div>

    <svg class="motto" viewBox="0 0 400 400" aria-hidden="true">
      <defs>
        <path id="motto-arc" d="M 48.4 112.5 A 175 175 0 0 1 351.6 112.5"/>
      </defs>
      <text><textPath href="#motto-arc" startOffset="50%" text-anchor="middle">ANYTIME IS COFFEE TIME</textPath></text>
    </svg>

    <div class="cup-art" role="img" aria-label="Illustration of a white cup of black coffee seen from above"></div>

    <div class="address-strip">
      <span>47 W. Oak Ave., Dunmore, WI 54921</span>
      <span>www.heronlanecoffee.example</span>
    </div>
  </main>
</body>
</html>
```